Professional Services - letterhead / business cards

The company (veltaro holdings) will provide services to Investment Funds and large investors in Spain. I have recently chosen a logo that I am attaching.

I would like a simple stationary design that i could use as letter head, business cards and "with compliments" cards.

I am not quite sure which color I will mostly use for the logo, in the email signature I will probably lean towards the white background and grey letters. I am attaching my favourite options.

Target Market(s)

Large Multinationals, Investment funds and Law firms

Industry/Entity Type

Business

Requirements
Must have
• my details are:
Luis R. Andrade
Veltaro Holdings S.L.
Casa de Valdehondo
Calle del Olmo Tardío 42
28017 Madrid
T: +34 (91) 807-3356
M: +34 (655) 718-904
e-mail: landrade@veltaroholdings.example

```html
<!DOCTYPE html>
<html lang="en">
<head>
<meta charset="utf-8">
<title>Veltaro Holdings — Stationery</title>
<link href="https://fonts.googleapis.com/css2?family=Questrial&family=Source+Sans+3:wght@400;600&display=swap" rel="stylesheet">
<style>
  :root {
    --backdrop: #ebebeb;
    --paper: #f4f4f4;
    --ink-navy: #2b2a6b;
    --ink-grey: #6e6e6e;
    --ink-dark: #3c3c3c;
    --slate: #4a4a4a;
    --window: #e3e3e3;
    --window-edge: #cfcfcf;
  }
  * { box-sizing: border-box; margin: 0; padding: 0; }
  html, body { width: 1200px; height: 750px; overflow: hidden; background: var(--backdrop); }
  .canvas { position: relative; width: 1200px; height: 750px; }
  .sheet { position: absolute; background: var(--paper); }
  .brand { font-family: "Questrial", sans-serif; color: var(--ink-navy); white-space: nowrap; letter-spacing: 0.2px; }
  .brand.light { color: #ffffff; }

  /* Letterhead */
  .letterhead { left: 113px; top: 37px; width: 457px; height: 649px; }
  .letterhead .brand { position: absolute; left: 27px; top: 30px; font-size: 24px; }
  .letter-body {
    position: absolute; left: 64px; top: 166px; width: 335px;
    font-family: "Source Sans 3", sans-serif; font-size: 9.2px; line-height: 11.2px; color: var(--ink-grey);
  }
  .letter-body p { margin-bottom: 11px; }
  .letter-body .gap { margin-bottom: 22px; }
  .signature { display: block; width: 60px; height: 26px; margin-top: 8px; background: linear-gradient(90deg, #d9d8e8, #c9c8e0); border-radius: 3px; }
  .letter-footer {
    position: absolute; left: 27px; bottom: 21px; width: 410px;
    font-family: "Source Sans 3", sans-serif; font-size: 6.6px; color: var(--ink-dark);
    display: flex; gap: 6px; align-items: center; white-space: nowrap;
  }
  .dot { display: inline-block; width: 7px; height: 7px; border-radius: 50%; background: var(--ink-navy); vertical-align: middle; margin-right: 2px; }

  /* Envelopes */
  .envelope-back { left: 611px; top: 39px; width: 512px; height: 244px; }
  .envelope-back svg { position: absolute; left: 0; top: 0; }
  .envelope-back .brand { position: absolute; left: 0; width: 512px; top: 35px; text-align: center; font-size: 15px; }
  .envelope-front { left: 611px; top: 303px; width: 512px; height: 246px; }
  .envelope-front .brand { position: absolute; left: 23px; top: 27px; font-size: 19px; }
  .return-address {
    position: absolute; left: 23px; top: 78px;
    font-family: "Source Sans 3", sans-serif; font-size: 6.8px; line-height: 8px; color: var(--ink-dark);
  }
  .address-window {
    position: absolute; left: 23px; top: 108px; width: 136px; height: 49px;
    background: var(--window); border: 1px solid var(--window-edge); border-radius: 7px;
  }

  /* Business cards */
  .card { top: 568px; width: 208px; height: 118px; }
  .card-front { left: 611px; }
  .card-front .brand { position: absolute; left: 12px; top: 18px; font-size: 12px; }
  .card-details {
    position: absolute; left: 12px; top: 66px;
    font-family: "Source Sans 3", sans-serif; font-size: 5px; line-height: 6.4px; color: var(--ink-dark);
  }
  .card-details .contact { margin-top: 5px; }
  .card-details .dot { width: 5px; height: 5px; }
  .card-name {
    position: absolute; right: 12px; top: 66px;
    font-family: "Source Sans 3", sans-serif; font-weight: 600; font-size: 7.4px; color: var(--ink-navy);
  }
  .card-tab { position: absolute; right: 0; top: 61px; width: 4px; height: 20px; background: var(--ink-navy); }
  .card-back { left: 842px; background: var(--slate); }
  .card-back .brand { position: absolute; left: 0; width: 205px; top: 52px; text-align: center; font-size: 12px; }
</style>
</head>
<body>
<main class="canvas">

  <section class="sheet letterhead" aria-label="Letterhead">
    <div class="brand">veltaro holdings</div>
    <div class="letter-body">
      <p class="gap">Your Street Address<br>Your City, State&nbsp; Zip<br>Date</p>
      <p class="gap">First and Last Name of the Person to whom you are writing<br>Their Street Address<br>City, ST Zip</p>
      <p>Dear Mr./Ms. Full Name:</p>
      <p class="gap">You do not want to indent when you are using this format. This is the best format to use when you are writing a persuasive letter. You want to introduce yourself and the topic you are writing about to the reader. Remember that the first rule of writing is to know your audience. In a persuasive letter, you state your opinion or your feelings about something that is important to you after you have introduced yourself. You must sound as professional and passionate as possible. You do not want to belittle the reader or they will not finish reading your letter. Your letter needs to have the facts, reasons, and examples to support your position. Address issues that your reader may have in their argument.<br>In a second paragraph, you must have solutions. Without solutions, you are only complaining. Offer assistance in solving the problem. Remind the reader where they can contact you.</p>
      <p>Sincerely yours,</p>
      <span class="signature" role="img" aria-label="Handwritten signature"></span>
    </div>
    <div class="letter-footer">
      <span>Calle del Olmo Tardío 42. Casa de Valdehondo. 28017 Madrid</span>
      <span><i class="dot"></i>+34 (91) 807-3356</span>
      <span><i class="dot"></i>+34 (655) 718-904</span>
      <span><i class="dot"></i>landrade@veltaroholdings.example</span>
    </div>
  </section>

  <section class="sheet envelope-back" aria-label="Envelope, back">
    <svg width="512" height="82" viewBox="0 0 512 82" aria-hidden="true">
      <polygon points="0,0 512,0 512,12 500,82 12,82 0,12" fill="#4a4a4a"/>
    </svg>
    <div class="brand light">veltaro holdings</div>
  </section>

  <section class="sheet envelope-front" aria-label="Envelope, front">
    <div class="brand">veltaro holdings</div>
    <div class="return-address">Calle del Olmo Tardío 42<br>Casa de Valdehondo<br>28017 Madrid</div>
    <div class="address-window"></div>
  </section>

  <section class="sheet card card-front" aria-label="Business card, front">
    <div class="brand">veltaro holdings</div>
    <div class="card-details">
      Calle del Olmo Tardío 42<br>Casa de Valdehondo<br>28017 Madrid
      <div class="contact">
        <i class="dot"></i>+34 (91) 807-3356 &nbsp;<i class="dot"></i>+34 (655) 718-904<br>
        <i class="dot"></i>landrade@veltaroholdings.example
      </div>
    </div>
    <div class="card-name">Luis R. Andrade</div>
    <div class="card-tab"></div>
  </section>

  <section class="sheet card card-back" aria-label="Business card, back">
    <div class="brand light">veltaro holdings</div>
  </section>

</main>
</body>
</html>
```